Data Analytics Platform Website Design

Website design for a new data analytics platform called Metricvale Hub. I need a design that is simple but informative, professional but still sexy and that is aimed at the business professional instead of being "technical". I have a logo (picture uploaded) and also screenshots from the platform itself and I can also provide example websites from competitors that are similar in design and layout to what I need. I also have the messaging but I need help with photos, icons, font, layout, etc. I want to utilize some of the colors in the logo, but I want the overall color scheme to utilize darker blues (more serious feeling, less playful) with one accent color for highlighting. This design cannot be "fun", "playful", or "cheerful" and should instead be "professional", "serious", but still uncluttered and clean cut. However, simple does not mean easy because I want to see transitions that are clean and high level. I want the final design to be all of that while showing the company and our product as capable, serious, and reliable.

Example websites:
1. www.brantolux.com
2. q7.ai
3. velmoristo.com
4. https://www.ryk.com/en_us/software/dolen.html
5. https://www.pelvoro.com/
6. lisbet.ai

Target Market(s)

Business Professionals - Government/large companies/data analytics focused

Industry/Entity Type

Data Science

Number of Pages Required

3 page

Font styles to use
Serif
Sans Serif

Requirements
Must have
• It must be clean and professional. Cannot be cluttered or too "busy". No playful or childish looks at all.
Nice to have
• I want to see professional designs but also professional concepts incorporated.
Should not have
• Should not have Comic Sans or the like, no playful or "techy" themes

```html
<!DOCTYPE html>
<html lang="en">
<head>
<meta charset="utf-8">
<title>Metricvale Hub — Data Analytics Platform</title>
<link rel="stylesheet" href="https://fonts.googleapis.com/css2?family=Jost:ital,wght@0,400;0,500;0,600;0,700;1,400&display=swap">
<style>
:root{
  --navy-900:#060b2e;
  --navy-800:#0a1240;
  --navy-700:#0d1749;
  --navy-600:#141d52;
  --card:#111a4c;
  --card-line:#2a3470;
  --band:#1b2358;
  --accent:#3d6ef2;
  --accent-2:#7a5cf0;
  --white:#ffffff;
  --muted:#c9cfe8;
}
*{margin:0;padding:0;box-sizing:border-box}
html,body{width:1200px;height:5236px;overflow:hidden}
body{background:var(--navy-800);color:var(--white);font-family:"Jost",sans-serif;position:relative}
section,header,footer{position:absolute;left:0;width:1200px;overflow:hidden}
.abs{position:absolute}
.btn{position:absolute;display:flex;align-items:center;justify-content:center;background:var(--accent);color:var(--white);border-radius:24px;font-size:14px;font-weight:500}
.btn-outline{background:transparent;border:2px solid var(--accent)}
.h2{font-size:38px;font-weight:500;line-height:1.2}
.rule{position:absolute;width:70px;height:3px;background:linear-gradient(90deg,var(--accent-2),var(--accent))}
.center{left:0;width:1200px;text-align:center}
.body-text{font-size:14.5px;line-height:26.5px;color:var(--white)}
.shot{position:absolute}

/* hero */
.hero{top:0;height:728px;background:var(--navy-900)}
.hero-photo{left:0;top:0;width:1200px;height:728px;background:radial-gradient(ellipse at 50% 40%,#2a4a6e 0%,#15294a 40%,#0a1530 80%)}
.nav{top:0;height:90px;width:1200px}
.brand{left:112px;top:24px;display:flex;align-items:center;gap:10px;font-size:25px;font-weight:400}
.brand-mark{width:18px;height:18px;background:var(--accent)}
.nav-link{top:31px;font-size:14px}
.hero-title{left:618px;top:240px;font-size:66px;font-weight:700;line-height:68px}
.hero-text{left:620px;top:393px;width:480px;font-size:15px;line-height:26px}

/* about */
.about{top:728px;height:619px;background:var(--navy-800)}
.about-screen{left:488px;top:126px;width:600px;height:362px;border-radius:14px;background:linear-gradient(135deg,#e8ecf5 0%,#cfd6e6 60%,#1e2538 100%)}

/* solutions */
.solutions{top:1347px;height:677px;background:var(--navy-700)}
.sol-card{top:233px;width:224px;height:271px;background:var(--card);border:1px solid var(--card-line);border-radius:4px;text-align:center}
.sol-icon{position:absolute;left:80px;top:64px;width:64px;height:64px;border-radius:12px;background:linear-gradient(135deg,#3d6ef2,#2aa6f5)}
.sol-label{position:absolute;left:0;width:100%;top:152px;font-size:18px;font-weight:500;line-height:27px}

/* video */
.video{top:2024px;height:763px;background:var(--navy-800)}
.video-frame{left:183px;top:278px;width:832px;height:397px;border-radius:14px;border:1px solid #2b3a7a;background:radial-gradient(ellipse at 35% 55%,#1d7fd6 0%,#0f3a7a 35%,#08163e 75%)}
.play{left:560px;top:438px;width:80px;height:80px;background:var(--white);border-radius:10px}

/* stories */
.stories{top:2787px;height:528px;background:var(--navy-700)}
.story-card{left:445px;top:81px;width:584px;height:376px;background:linear-gradient(90deg,#0c1230 0%,#121a3a 50%,#2b3350 100%)}
.arrow{top:311px;width:56px;height:56px;border:2px solid var(--accent);border-radius:50%}

/* feature */
.feature{top:3315px;height:539px;background:var(--navy-800)}
.feature-img{left:112px;top:76px;width:417px;height:396px;background:radial-gradient(ellipse at 45% 55%,#1f6fd0 0%,#0f3272 40%,#0a1746 80%)}

/* dive */
.dive{top:3854px;height:777px;background:var(--navy-700)}
.post-img{top:175px;width:307px;height:230px}
.post-title{top:430px;width:307px;font-size:17px;line-height:26px;font-weight:500}
.post-text{top:500px;width:307px;font-size:13.5px;line-height:26px}
.read{top:590px;display:flex;align-items:center;gap:12px;color:var(--accent);font-size:14px;font-weight:500}
.plus{width:20px;height:20px;border-radius:50%;background:var(--accent);color:#fff;display:flex;align-items:center;justify-content:center;font-size:15px}

/* partners */
.partners{top:4631px;height:129px;background:var(--band)}
.partner{top:44px;display:flex;align-items:center;gap:12px;font-size:24px;font-weight:500;color:#d3d8ee}
.partner i{width:28px;height:28px;border-radius:50%;background:#d3d8ee;display:block}

/* footer */
.footer{top:4760px;height:476px;background:var(--navy-800)}
.col-head{top:68px;font-size:17px;font-weight:500}
.col-list{top:108px;list-style:none;font-size:13.5px;line-height:32.5px;color:var(--muted)}
.news{left:112px;top:340px;font-size:14px;line-height:24px}
.input{left:362px;top:345px;width:279px;height:46px;border-radius:23px;background:#fff;color:#555;font-size:13.5px;padding:14px 18px}
.social{top:346px;width:44px;height:44px;border-radius:50%;background:#1d2660}
.divider{left:112px;top:418px;width:974px;height:1px;background:#232d66}
.legal{top:438px;font-size:12px;color:var(--muted)}
</style>
</head>
<body>

<header class="hero">
  <div class="abs hero-photo" role="img" aria-label="Businessman in a suit standing before large glowing data dashboards"></div>
  <div class="abs brand"><span class="brand-mark"></span>Metricvale Hub</div>
  <span class="abs nav-link" style="left:423px">Platforms</span>
  <span class="abs nav-link" style="left:532px">Solutions</span>
  <span class="abs nav-link" style="left:637px">Learn</span>
  <span class="abs nav-link" style="left:718px">Community</span>
  <span class="abs nav-link" style="left:838px">Company</span>
  <span class="btn btn-outline" style="left:948px;top:20px;width:138px;height:45px">Get Started</span>
  <h1 class="abs hero-title">Data Analytics<br>Platform</h1>
  <p class="abs hero-text">Lorem ipsum dolor sit amet consectetur adipiscing elit sed do eiusmod tempor incididunt ut labore et dolore magna.</p>
  <span class="btn" style="left:620px;top:482px;width:200px;height:44px">Download The Report</span>
</header>

<section class="about">
  <svg class="abs" style="left:900px;top:0" width="300" height="619" viewBox="0 0 300 619" aria-hidden="true">
    <path d="M80 120 A300 300 0 0 1 300 12" fill="none" stroke="#6b4fd8" stroke-width="1.5"/>
    <path d="M70 480 A300 300 0 0 0 300 618" fill="none" stroke="#3d6ef2" stroke-width="1.5"/>
  </svg>
  <h2 class="abs h2" style="left:112px;top:142px">About Metricvale Hub</h2>
  <div class="rule" style="left:112px;top:200px"></div>
  <p class="abs body-text" style="left:112px;top:216px;width:372px">Lorem ipsum dolor sit amet, consectetur adipiscing elit, sed do to do eiusmod tempor incididunt ut it labore et dolore magna aliqua. Ut ad minim to veniam, quis nostrud exercitation ullamco laboris nisi ut aliquip ex ea commodo consequat. Duis aute irure dolor in reprehenderit in voluptate velit esse cillum dolore eu fugiat nulla pariatur.</p>
  <span class="btn" style="left:112px;top:429px;width:146px;height:47px">Read More</span>
  <div class="shot about-screen" role="img" aria-label="Laptop showing the platform's organization administration screen"></div>
</section>

<section class="solutions">
  <h2 class="abs h2 center" style="top:66px">Our Solutions</h2>
  <div class="rule" style="left:565px;top:124px"></div>
  <p class="abs center" style="top:136px;font-size:14.5px;line-height:26px">Lorem ipsum dolor sit amet, consectetur adipiscing elit, sed do to do<br>eiusmod tempor incididunt ut labore et dolore magna aliqua.</p>
  <div class="abs sol-card" style="left:112px"><div class="sol-icon" role="img" aria-label="Observability network icon"></div><div class="sol-label">Intelligent<br>Observability</div></div>
  <div class="abs sol-card" style="left:362px"><div class="sol-icon" role="img" aria-label="Team collaboration icon"></div><div class="sol-label">Team<br>Collaboration</div></div>
  <div class="abs sol-card" style="left:612px"><div class="sol-icon" role="img" aria-label="AI assistant robot icon"></div><div class="sol-label">AI<br>Assistance</div></div>
  <div class="abs sol-card" style="left:862px"><div class="sol-icon" role="img" aria-label="Business analytics chart icon"></div><div class="sol-label">Business<br>Analytics</div></div>
  <span class="btn" style="left:522px;top:553px;width:156px;height:46px">Explore More</span>
</section>

<section class="video">
  <h2 class="abs h2 center" style="top:66px;line-height:48px">Get Back to the Basics with Metricvale Hub<br>Endpoint Management and Security Platform</h2>
  <div class="rule" style="left:565px;top:169px"></div>
  <p class="abs center" style="top:184px;font-size:14.5px;line-height:26px">Lorem ipsum dolor sit amet, consectetur adipiscing elit, sed do to do eiusmod<br>tempor incididunt ut labore et dolore magna aliqua.</p>
  <div class="abs video-frame" role="img" aria-label="Hands holding a tablet projecting glowing analytics charts over a city"></div>
  <div class="abs play"><svg width="80" height="80" viewBox="0 0 80 80" aria-label="Play video"><path d="M30 22 L58 40 L30 58 Z" fill="#3d6ef2"/></svg></div>
</section>

<section class="stories">
  <h2 class="abs h2" style="left:112px;top:156px">Customer Stories</h2>
  <div class="rule" style="left:112px;top:212px"></div>
  <p class="abs" style="left:112px;top:226px;font-size:14.5px;line-height:24px">Real stories, amazing people.<br>Hear from our customers.</p>
  <div class="abs arrow" style="left:112px"><svg width="52" height="52" viewBox="0 0 52 52" aria-label="Previous"><path d="M29 19 L22 26 L29 33" fill="none" stroke="#fff" stroke-width="2"/></svg></div>
  <div class="abs arrow" style="left:182px"><svg width="52" height="52" viewBox="0 0 52 52" aria-label="Next"><path d="M23 19 L30 26 L23 33" fill="none" stroke="#fff" stroke-width="2"/></svg></div>
  <div class="abs story-card" role="img" aria-label="Portrait of a confident customer in a suit in an office"></div>
  <p class="abs" style="left:480px;top:164px;width:340px;font-size:14.5px;line-height:26.5px;font-style:italic">Lorem ipsum dolor sit amet sit adipiscing elit to sed do eiusmod tempor to incide cidiut labore et dolore magna aliqua. Quis ipsum suspend ultrices gravida. Risus commodo viverra map accumsan lacus vel facilisis.</p>
  <span class="btn" style="left:480px;top:325px;width:136px;height:43px">Watch Story</span>
</section>

<section class="feature">
  <div class="abs feature-img" role="img" aria-label="Glowing smartphone displaying market data charts"></div>
  <h2 class="abs h2" style="left:584px;top:106px">Lorem Ipsum dolar Sit</h2>
  <div class="rule" style="left:586px;top:163px"></div>
  <p class="abs body-text" style="left:584px;top:176px;width:504px">Lorem ipsum dolor sit amet, consectetur adipiscing elit, sed do to do eiusmod tempor incididunt ut labore et dolore magna aliqua. Ut ad mini veniam, quis nostrud exercitation ullamco laboris nisi ut aliquip ex ea commodo consequat. Duis aute irure dolor in reprehenderit in voluptate velit esse cillum dolore eu fugiat nulla pariatur. Excepteur sint occaecat cupidatat non proident, sunt in culpa qui official deserunt mollit anim id est laborum sed ut perspiciatis.</p>
  <span class="btn" style="left:586px;top:389px;width:146px;height:46px">Read More</span>
</section>

<section class="dive">
  <h2 class="abs h2 center" style="top:70px">Dive Into the New Age</h2>
  <div class="rule" style="left:565px;top:127px"></div>

  <div class="abs post-img" style="left:112px;background:radial-gradient(ellipse at 55% 55%,#6a6ee0 0%,#2c3a9a 45%,#0c1650 85%)" role="img" aria-label="Glowing digital globe"></div>
  <h3 class="abs post-title" style="left:112px">Many desktop publishing package and web page editors</h3>
  <p class="abs post-text" style="left:112px">Lorem ipsum dolor sit amet consectetur sed adipiscing elit sed do to do eiusmod tempor incididunt ut labore et dolore.</p>
  <div class="abs read" style="left:112px">Read More <span class="plus">+</span></div>

  <div class="abs post-img" style="left:445px;background:linear-gradient(180deg,#3a5a72 0%,#1d3346 50%,#3a3530 100%)" role="img" aria-label="Analyst standing before trading screens"></div>
  <h3 class="abs post-title" style="left:445px">Many desktop publishing package and web page editors</h3>
  <p class="abs post-text" style="left:445px">Lorem ipsum dolor sit amet consectetur sed adipiscing elit sed do to do eiusmod tempor incididunt ut labore et dolore.</p>
  <div class="abs read" style="left:445px">Read More <span class="plus">+</span></div>

  <div class="abs post-img" style="left:779px;background:linear-gradient(135deg,#3f7fbf 0%,#1f4f86 50%,#16335c 100%)" role="img" aria-label="Businessman facing a wall of data charts and a world map"></div>
  <h3 class="abs post-title" style="left:779px">Many desktop publishing package and web page editors</h3>
  <p class="abs post-text" style="left:779px">Lorem ipsum dolor sit amet consectetur sed adipiscing elit sed do to do eiusmod tempor incididunt ut labore et dolore.</p>
  <div class="abs read" style="left:779px">Read More <span class="plus">+</span></div>

  <span class="btn btn-outline" style="left:510px;top:658px;width:180px;height:48px">More Community</span>
</section>

<section class="partners">
  <div class="abs partner" style="left:148px"><i></i>Norvik</div>
  <div class="abs partner" style="left:407px"><i></i>Tessaline</div>
  <div class="abs partner" style="left:655px"><i></i>Quorbane</div>
  <div class="abs partner" style="left:911px"><i></i>Ambrelo</div>
</section>

<footer class="footer">
  <h4 class="abs col-head" style="left:112px">Quick Links</h4>
  <ul class="abs col-list" style="left:112px"><li>Platforms</li><li>Solutions</li><li>Learn</li><li>Community</li><li>Company</li></ul>
  <h4 class="abs col-head" style="left:303px">Solutions</h4>
  <ul class="abs col-list" style="left:303px"><li>Intelligent Observability</li><li>Team Collaboration</li><li>AI Assistance</li><li>BusinessAnalytics</li></ul>
  <h4 class="abs col-head" style="left:557px">Community</h4>
  <ul class="abs col-list" style="left:557px"><li>Community 1</li><li>Community 2</li><li>Community 3</li><li>Community 4</li></ul>
  <h4 class="abs col-head" style="left:746px">Learn</h4>
  <ul class="abs col-list" style="left:746px"><li>Customer Stories</li><li>Blog</li><li>How To Get Started</li><li>Partnership</li></ul>
  <h4 class="abs col-head" style="left:968px">Company</h4>
  <ul class="abs col-list" style="left:968px"><li>About</li><li>Leadership Team</li><li>Investors</li><li>Career</li></ul>

  <p class="abs news">Become an Insider<br>Subscribe to our newsletter</p>
  <div class="abs input">Enter Email</div>
  <span class="btn" style="left:655px;top:345px;width:136px;height:46px">Subscribe</span>
  <span class="abs social" style="left:859px" aria-label="Social link"></span>
  <span class="abs social" style="left:916px" aria-label="Social link"></span>
  <span class="abs social" style="left:971px" aria-label="Social link"></span>
  <span class="abs social" style="left:1028px" aria-label="Social link"></span>
  <div class="abs divider"></div>
  <p class="abs legal" style="left:112px">Privacy Policy &nbsp;| Legal</p>
  <p class="abs legal" style="right:114px">Copyright © 2021 <span style="color:var(--accent)">Metricvale Hub</span>. All Rights Reserved.</p>
</footer>

</body>
</html>
```